Business card design for online Mandarin Learning School

We need a business card design for our online language learning school called "Maple Bridge Online for Mandarin Learning". Our existing website is https://www.maplebridgeonline.com
We have our logo already. We would like to see our business card design that can make our online teaching services to be innovative, young, energetic and fun to learn. Prefer to have a certain level of color matching with our website. Apart from "Maple Bridge Online", need to specifically state "for Mandarin Learning" as well on the business card.

```html
<!DOCTYPE html>
<html lang="en">
<head>
<meta charset="UTF-8">
<title>Maple Bridge Online – Business Card</title>
<link href="https://fonts.googleapis.com/css2?family=Marcellus&family=Open+Sans:wght@400;600&display=swap" rel="stylesheet">
<style>
  :root {
    --teal: #13a3ad;
    --coral: #e5605c;
    --grey: #8c8c8c;
    --ink: #4a4a4a;
    --white: #ffffff;
    --backdrop: #2e3033;
  }
  * { margin: 0; padding: 0; box-sizing: border-box; }
  html, body { width: 1200px; height: 900px; overflow: hidden; }
  body {
    background: var(--backdrop);
    display: flex;
    align-items: center;
    justify-content: center;
    gap: 60px;
  }
  .card {
    position: relative;
    width: 520px;
    height: 300px;
    border-radius: 26px;
    overflow: hidden;
    box-shadow: 0 18px 40px rgba(0,0,0,.45);
  }

  /* Front: contact side */
  .card-front { background: var(--white); }
  .front-band {
    position: absolute; left: 0; right: 0; bottom: 0; height: 42px;
    background: linear-gradient(90deg, var(--teal) 0%, #9aa3a4 40%, var(--grey) 55%, var(--coral) 85%);
  }
  .person { position: absolute; left: 34px; top: 34px; }
  .person-name {
    font-family: "Marcellus", serif;
    font-size: 21px; color: var(--ink); letter-spacing: 1px;
  }
  .person-title {
    font-family: "Open Sans", sans-serif;
    font-size: 11px; color: var(--coral); letter-spacing: 1px; margin-top: 2px;
  }
  .name-rule {
    position: absolute; left: 178px; right: 0; top: 66px;
    height: 2px; background: var(--teal);
  }
  .contact-list { list-style: none; position: absolute; left: 34px; top: 92px; }
  .contact-item {
    display: flex; align-items: center; gap: 8px;
    font-family: "Open Sans", sans-serif; font-size: 12px; color: var(--ink);
    margin-bottom: 6px;
  }
  .contact-icon { width: 11px; height: 11px; flex: none; }
  .brand-block {
    position: absolute; right: 40px; top: 166px;
    display: flex; flex-direction: column; align-items: flex-end;
  }
  .brand-mark { display: flex; align-items: center; gap: 10px; }
  .brand-dot { width: 12px; height: 12px; border-radius: 50%; background: var(--coral); }
  .brand-name {
    font-family: "Marcellus", serif; font-size: 24px;
    color: var(--teal); letter-spacing: 2px; line-height: 1.1;
  }
  .brand-tagline {
    font-family: "Marcellus", serif; font-size: 12px;
    color: var(--grey); letter-spacing: 1.5px; margin-top: 3px;
  }
  .front-web {
    position: absolute; right: 40px; bottom: 54px;
    font-family: "Open Sans", sans-serif; font-size: 13px; color: var(--ink);
  }

  /* Back: brand side */
  .card-back {
    background: linear-gradient(110deg, var(--teal) 0%, var(--teal) 22%, #9b9b9b 45%, #b0a3a2 55%, var(--coral) 78%, var(--coral) 100%);
  }
  .back-strip {
    position: absolute; left: 0; right: 0; top: 50px; height: 136px;
    background: var(--white);
    display: flex; flex-direction: column; align-items: flex-end; justify-content: center;
    padding-right: 42px;
  }
  .back-name {
    font-family: "Marcellus", serif; font-size: 38px;
    color: var(--teal); letter-spacing: 2px; line-height: 1;
  }
  .back-rule { display: flex; width: 300px; height: 4px; margin: 6px 0 5px; }
  .back-rule span:first-child { flex: 1; background: var(--coral); }
  .back-rule span:last-child { flex: 2; background: var(--grey); }
  .back-web {
    font-family: "Marcellus", serif; font-size: 16px;
    color: var(--coral); letter-spacing: 1px;
  }
  .back-web-rule { width: 300px; height: 3px; background: var(--teal); margin-top: 3px; }
  .back-tagline {
    font-family: "Marcellus", serif; font-size: 13px;
    color: var(--grey); letter-spacing: 2px; margin-top: 7px;
  }
</style>
</head>
<body>

  <section class="card card-front" aria-label="Business card, contact side">
    <div class="person">
      <div class="person-name">YOUR NAME</div>
      <div class="person-title">JOB TITLE</div>
    </div>
    <div class="name-rule"></div>
    <ul class="contact-list">
      <li class="contact-item">
        <svg class="contact-icon" viewBox="0 0 12 12"><rect width="12" height="12" rx="2" fill="#e5605c"/><path d="M3 4.5c0-1 1-1.5 3-1.5s3 .5 3 1.5v.5H7.5v-.5h-3v.5H3zM3.5 6h5l.5 3h-6z" fill="#fff"/></svg>
        000 000 0000
      </li>
      <li class="contact-item">
        <svg class="contact-icon" viewBox="0 0 12 12"><rect x="3" y="0.5" width="6" height="11" rx="1.2" fill="none" stroke="#e5605c" stroke-width="1.2"/><circle cx="6" cy="9.5" r=".7" fill="#e5605c"/></svg>
        000 000 0000
      </li>
      <li class="contact-item">
        <svg class="contact-icon" viewBox="0 0 12 12"><rect width="12" height="12" rx="2" fill="#e5605c"/><path d="M2.5 4l3.5 2.5L9.5 4" fill="none" stroke="#fff" stroke-width="1.1"/></svg>
        youremail@maplebridgeonline.com
      </li>
    </ul>
    <div class="brand-block">
      <div class="brand-mark">
        <span class="brand-dot"></span>
        <span class="brand-name">MAPLE BRIDGE</span>
      </div>
      <div class="brand-tagline">FOR MANDARIN LEARNING</div>
    </div>
    <div class="front-web">www.maplebridgeonline.com</div>
    <div class="front-band"></div>
  </section>

  <section class="card card-back" aria-label="Business card, brand side">
    <div class="back-strip">
      <div class="back-name">MAPLE BRIDGE</div>
      <div class="back-rule"><span></span><span></span></div>
      <div class="back-web">WWW.MAPLEBRIDGEONLINE.COM</div>
      <div class="back-web-rule"></div>
      <div class="back-tagline">FOR MANDARIN LEARNING</div>
    </div>
  </section>

</body>
</html>
```